Tennard Executive Action Post card

I am an immigration attorney. President TENNARD is about to announce an immigration benefit in the next sixty days. I want a Postcard with Tennard photo speaking (bubble thought or something like that) that in spanish says something like. Hey, i already gave the order....and in the inside it would follow with "Now call Ernesto Callejas. the inside might have my logo, my address and my telepone and some sort of slogan.

Target Market(s)

Hispanic clientele, not very sophistacated.

Industry/Entity Type

Attorney

Font styles to use
Sans Serif

Colors

Designer to choose colors to be used in the design.

Requirements
Must have
• TENNARD
Spanish text
My logo
Easy to read telephone and address
Ernesto L. Callejas-Abogado de Inmigracion
20 Anos de Experiencia
17 Birchfold Avenue Waltham MA 02197
555-013-7261
Nice to have
• Im looking for funny, and entertaining....not serious and elegant

```html
<!DOCTYPE html>
<html lang="es">
<head>
<meta charset="utf-8">
<title>Tennard Acción Ejecutiva – Postal</title>
<link rel="stylesheet" href="https://fonts.googleapis.com/css2?family=Comic+Neue:wght@400;700&family=Open+Sans:ital,wght@0,400;0,700;0,800;1,700&family=Roboto+Condensed:wght@400;700&display=swap">
<style>
  :root {
    --backdrop: #e6dfd2;
    --card-black: #000000;
    --headline-yellow: #f7e21a;
    --white: #ffffff;
    --ink: #1a1a1a;
    --phone-red: #e0202a;
    --navy: #1f3670;
    --logo-blue: #2f7fc4;
    --khaki: #c9bb8a;
    --quote-ink: #3b3a36;
    --rule-grey: #9a9a9a;
    --photo-dark: #2a221d;
    --photo-mid: #6b5142;
  }
  * { box-sizing: border-box; margin: 0; padding: 0; }
  html, body { width: 1200px; height: 500px; overflow: hidden; }
  body { background: var(--backdrop); position: relative; font-family: "Open Sans", Arial, sans-serif; }

  /* ---------- front of card ---------- */
  .card-front {
    position: absolute; left: 18px; top: 30px; width: 558px; height: 434px;
    background: var(--card-black); overflow: hidden;
  }
  .speaker-photo {
    position: absolute; left: 0; top: 30px; width: 260px; height: 404px;
    background: radial-gradient(ellipse at 45% 40%, var(--photo-mid) 0%, var(--photo-dark) 55%, var(--card-black) 90%);
  }
  .headline {
    position: absolute; left: 222px; top: 24px; width: 320px; text-align: center;
    font-family: "Roboto Condensed", Arial, sans-serif;
  }
  .headline-title { color: var(--headline-yellow); font-weight: 700; font-size: 27px; line-height: 32px; }
  .headline-sub { color: var(--white); font-weight: 400; font-size: 21px; line-height: 26px; }

  .speech-bubble { position: absolute; left: 198px; top: 88px; width: 342px; height: 316px; }
  .speech-text {
    position: absolute; left: 266px; top: 98px; width: 264px; white-space: nowrap;
    font-family: "Comic Neue", "Comic Sans MS", sans-serif; font-weight: 400;
    font-size: 22px; line-height: 27px; color: var(--ink);
  }
  .speech-text .phone { color: var(--phone-red); }
  .front-logo {
    position: absolute; left: 372px; top: 354px; display: flex; align-items: center; gap: 5px;
    font-family: "Open Sans", Arial, sans-serif; font-size: 7.5px; line-height: 9px;
    font-weight: 400; color: var(--navy); text-transform: uppercase;
  }
  .logo-dot { width: 12px; height: 12px; border-radius: 50%; background: var(--logo-blue); }

  /* ---------- back of card ---------- */
  .card-back {
    position: absolute; left: 612px; top: 30px; width: 560px; height: 434px;
    background: var(--white); overflow: hidden;
  }
  .flag-photo {
    position: absolute; left: 0; top: 0; width: 270px; height: 180px;
    background: linear-gradient(135deg, #1e2f6e 0%, #b8232f 38%, #e9e4dc 60%, #c7d8c4 80%, #e4e8ee 100%);
  }
  .slogan-panel {
    position: absolute; left: 0; top: 180px; width: 270px; height: 254px; background: var(--khaki);
  }
  .slogan {
    position: absolute; left: 30px; top: 12px; width: 232px;
    font-family: "Roboto Condensed", Arial, sans-serif; font-weight: 700;
    font-size: 13px; line-height: 16px; color: var(--quote-ink);
  }
  .attorney-name {
    position: absolute; left: 0; top: 130px; width: 270px; text-align: center;
    font-weight: 800; font-size: 18px; color: var(--navy); font-variant: small-caps; letter-spacing: 0.3px;
  }
  .attorney-role {
    position: absolute; left: 0; top: 158px; width: 270px; text-align: center;
    font-weight: 700; font-style: italic; font-size: 13px; color: var(--ink);
  }
  .attorney-years {
    position: absolute; left: 0; top: 183px; width: 270px; text-align: center;
    font-family: "Roboto Condensed", Arial, sans-serif; font-weight: 700; font-size: 15px; color: var(--phone-red);
  }
  .attorney-phone {
    position: absolute; left: 0; top: 204px; width: 270px; display: flex; justify-content: center; align-items: center; gap: 4px;
    font-weight: 700; font-size: 21px; color: var(--ink);
  }
  .return-address { position: absolute; left: 282px; top: 38px; width: 140px; }
  .return-logo {
    display: flex; align-items: center; gap: 5px;
    font-size: 8.5px; line-height: 10px; font-weight: 400; color: var(--navy); text-transform: uppercase;
  }
  .return-lines { margin-top: 6px; text-align: center; font-size: 11.5px; line-height: 14px; color: var(--ink); }
  .stamp-box { position: absolute; left: 420px; top: 6px; width: 121px; height: 145px; border: 1px solid var(--rule-grey); }
  .address-line { position: absolute; left: 303px; width: 238px; height: 0; border-top: 1px solid var(--rule-grey); }
</style>
</head>
<body>

  <section class="card-front" aria-label="Frente de la postal">
    <div class="speaker-photo" role="img" aria-label="Fotografía del presidente Tennard hablando"></div>

    <div class="headline">
      <h1 class="headline-title">Tennard Acción Ejecutiva</h1>
      <p class="headline-sub">Beneficios de la inmigración</p>
    </div>

    <svg class="speech-bubble" viewBox="0 0 342 316" aria-hidden="true">
      <path d="M67 2 H329 Q337 2 337 10 V302 Q337 310 329 310 H67 Q59 310 59 302 V258 L2 234 L59 222 V10 Q59 2 67 2 Z"
            fill="#ffffff" stroke="#bdbdbd" stroke-width="1.5"/>
    </svg>
    <p class="speech-text">¡Hey!, ya di la orden…<br>Consulte a Ernesto L.<br>Callejas, abogado de<br>inmigración con 20 años<br>de experiencia, llamando<br>al número <span class="phone">555.013.7261</span><br>o visítelo en su oficina<br>ubicada en 17 Birchfold<br>Avenue, Waltham, MA<br>02197</p>

    <div class="front-logo">
      <span class="logo-dot"></span>
      <span>Law Office of<br>Ernesto L. Callejas</span>
    </div>
  </section>

  <section class="card-back" aria-label="Reverso de la postal">
    <div class="flag-photo" role="img" aria-label="Bandera de Estados Unidos con tarjetas de residencia y seguro social"></div>

    <div class="slogan-panel">
      <p class="slogan">“A good immigration lawyer builds the bridge and then walks his clients across it.<br>An immigration lawyer can use his knowledge of the law and regulations and his experience to build a bridge that his clients can use to reach their immigration goals.”</p>
      <p class="attorney-name">Ernesto L. Callejas</p>
      <p class="attorney-role">Abogado de Inmigracion</p>
      <p class="attorney-years">20 Años de Experiencia</p>
      <p class="attorney-phone">
        <svg width="20" height="20" viewBox="0 0 20 20" aria-hidden="true">
          <circle cx="10" cy="10" r="9" fill="none" stroke="#1a1a1a" stroke-width="1.6"/>
          <path d="M7 5 L9 7.5 L8 9 Q9 11.5 11 12 L12.5 11 L15 13 L13.5 15 Q8 15 5 8 Z" fill="#1a1a1a"/>
        </svg>
        555.013.7261
      </p>
    </div>

    <div class="return-address">
      <div class="return-logo">
        <span class="logo-dot"></span>
        <span>The Law Office of<br>Ernesto L. Callejas</span>
      </div>
      <p class="return-lines">17 Birchfold Avenue,<br>Waltham,<br>MA 02197.</p>
    </div>

    <div class="stamp-box" aria-hidden="true"></div>
    <div class="address-line" style="top:232px"></div>
    <div class="address-line" style="top:267px"></div>
    <div class="address-line" style="top:302px"></div>
    <div class="address-line" style="top:337px"></div>
  </section>

</body>
</html>
```